Salt Moon, Tin Heart

Hey Guys
Please visit our Chatterleaf page for the film. See what ideas you bring to the table for the movie poster.
Looking for creative and something fresh.
Check out cast on QVTK
Will use the stills from the film for actual poster and quality.
Thanks a million for taking an interest in our film. xoxo
Target Market(s)
2-50 year old, date night, girls night out
Industry/Entity Type
Movie

```html
<!DOCTYPE html>
<html lang="en">
<head>
<meta charset="utf-8">
<title>Salt Moon, Tin Heart – Poster</title>
<link rel="stylesheet" href="https://fonts.googleapis.com/css2?family=Arimo:wght@400;700&display=swap">
<style>
  :root {
    --sun: #fff200;
    --lagoon: #14b2a6;
    --lagoon-deep: #0e8079;
    --olive-shade: #8d8731;
    --olive-dark: #55521e;
    --paper: #ffffff;
    --credit: #5a7f7c;
  }
  html, body {
    margin: 0;
    padding: 0;
    overflow: hidden;
    background: #e9e9e9;
  }
  .poster {
    position: relative;
    width: 710px;
    height: 1200px;
    overflow: hidden;
    font-family: "Arimo", Arial, sans-serif;
  }
  .band-top {
    position: absolute;
    left: 0; top: 0;
    width: 710px; height: 400px;
    background: var(--sun);
  }
  .band-bottom {
    position: absolute;
    left: 0; top: 798px;
    width: 710px; height: 402px;
    background: var(--lagoon);
  }
  .still {
    position: absolute;
    left: 0; top: 398px;
    width: 710px; height: 402px;
    display: block;
  }
  .cast {
    position: absolute;
    top: 18px; left: 0;
    width: 710px;
    display: flex;
    justify-content: center;
    gap: 46px;
    font-size: 30px;
    font-weight: 400;
    color: var(--credit);
  }
  .title-word {
    position: absolute;
    left: 0;
    width: 710px;
    margin: 0;
    text-align: center;
    font-weight: 700;
    font-size: 112px;
    line-height: 1;
    letter-spacing: 0.62em;
    text-indent: 0.62em;
  }
  .title-word.salt  { top: 150px; color: var(--lagoon); }
  .title-word.moon  { top: 282px; color: var(--paper); }
  .title-word.tin   { top: 836px; color: var(--sun); }
  .title-word.heart { top: 978px; color: var(--paper); letter-spacing: 0.4em; text-indent: 0.4em; }
</style>
</head>
<body>
<main class="poster">
  <div class="band-top"></div>
  <div class="band-bottom"></div>

  <svg class="still" viewBox="0 0 710 402" role="img" aria-label="Film still: a young man in a suit and a blonde woman facing each other at a dance, toned yellow on the left and teal on the right">
    <defs>
      <linearGradient id="warmTone" x1="0" y1="0" x2="1" y2="1">
        <stop offset="0" stop-color="var(--olive-shade)"/>
        <stop offset="1" stop-color="var(--olive-dark)"/>
      </linearGradient>
      <linearGradient id="coolTone" x1="0" y1="0" x2="1" y2="1">
        <stop offset="0" stop-color="var(--lagoon-deep)"/>
        <stop offset="1" stop-color="var(--lagoon)"/>
      </linearGradient>
    </defs>
    <rect width="710" height="402" fill="url(#coolTone)"/>
    <polygon points="0,0 710,0 710,70 150,402 0,402" fill="url(#warmTone)"/>
  </svg>

  <p class="cast"><span>Dara Whitfield</span><span>Colby Renner</span></p>

  <h1 class="title-word salt">SALT</h1>
  <p class="title-word moon">MOON</p>
  <p class="title-word tin">TIN</p>
  <p class="title-word heart">HEART</p>
</main>
</body>
</html>
```